Global Outreach Fellowship needs a Book Cover Design Project

I am a pastor, missionary, author, and the founder of a non-profit organization. I am in the process of publishing a book focused on "The Soul of a Faithful Shepherd" and desire a contemporary, even somewhat abstract book cover. Here is a link to the company's web page portfolio that designed our Web Page, to give you an idea of the style of cover that I am looking for. http://www.pixelharborstudio.com/cd-covers

Though the book is obviously targeted toward Christians, I want it to be attractive enough to capture the attention of the general population as well.

Industry/Entity Type

Non-Profit

```html
<!DOCTYPE html>
<html lang="en">
<head>
<meta charset="utf-8">
<title>The Soul of a Faithful Shepherd — Book Cover</title>
<link rel="stylesheet" href="https://fonts.googleapis.com/css2?family=Cinzel:wght@400;600&family=Cormorant+Garamond:ital,wght@0,500;1,500&display=swap">
<style>
  :root {
    --paper: #ffffff;
    --crop: #9a9a9a;
    --back-black: #000000;
    --sky-deep: #0b1f6e;
    --sky-mid: #1f4fc4;
    --sky-light: #6aa6ff;
    --glow: #e8f3ff;
    --band-dark: #120305;
    --band-edge: #2a0b10;
    --title-gold: #f0a43c;
    --title-lilac: #e2a6e6;
    --spine-white: #f4f6ff;
    --accent-orange: #f08a1c;
  }
  * { margin: 0; padding: 0; box-sizing: border-box; }
  html, body { width: 1200px; height: 900px; overflow: hidden; background: var(--paper); }
  .canvas { position: relative; width: 1200px; height: 900px; }

  .crop-mark { position: absolute; width: 1px; height: 32px; background: var(--crop); }
  .crop-mark.top { top: 100px; }
  .crop-mark.bottom { top: 768px; }
  .crop-mark.left { left: 580px; }
  .crop-mark.right { left: 620px; }

  .book {
    position: absolute; left: 184px; top: 132px; width: 832px; height: 636px;
    overflow: hidden;
    background:
      radial-gradient(ellipse 260px 320px at 646px 188px, rgba(232,243,255,0.95) 0%, rgba(140,190,255,0.55) 35%, rgba(40,90,210,0) 75%),
      radial-gradient(ellipse 520px 420px at 560px 120px, rgba(90,150,255,0.55) 0%, rgba(20,60,180,0) 70%),
      linear-gradient(180deg, var(--sky-mid) 0%, var(--sky-deep) 78%, #050a28 100%);
  }
  .rays {
    position: absolute; inset: 0;
    background: repeating-conic-gradient(from 0deg at 646px 188px, rgba(255,255,255,0.10) 0deg 3deg, rgba(255,255,255,0) 3deg 9deg);
    -webkit-mask-image: radial-gradient(ellipse 420px 380px at 646px 188px, #000 0%, transparent 80%);
            mask-image: radial-gradient(ellipse 420px 380px at 646px 188px, #000 0%, transparent 80%);
  }
  .back-cover {
    position: absolute; left: 0; top: 0; width: 240px; height: 100%;
    background: var(--back-black);
  }
  .winged-heart {
    position: absolute; left: 496px; top: 108px; width: 260px; height: 310px;
    background: radial-gradient(ellipse 50% 48% at 50% 40%, rgba(255,255,255,0.95) 0%, rgba(220,232,250,0.85) 45%, rgba(150,190,245,0) 100%);
  }

  .spine-title {
    position: absolute; left: 412px; top: 40px;
    display: flex; flex-direction: column; align-items: center; gap: 12px;
  }
  .spine-mark { width: 10px; height: 10px; background: var(--accent-orange); }
  .spine-text {
    writing-mode: vertical-rl;
    font-family: "Cinzel", serif; font-size: 15px; letter-spacing: 0.5px;
    color: var(--spine-white); white-space: nowrap;
  }

  .title-band {
    position: absolute; left: 0; top: 504px; width: 100%; height: 68px;
    background: linear-gradient(180deg, var(--band-edge) 0%, var(--band-dark) 20%, var(--band-dark) 80%, var(--band-edge) 100%);
    box-shadow: 0 -4px 10px rgba(90,30,60,0.45), 0 4px 10px rgba(90,30,60,0.35);
  }
  .front-title {
    position: absolute; right: 36px; top: 6px; text-align: right; line-height: 1;
  }
  .front-title .lead {
    display: block; margin-right: 60px;
    font-family: "Cormorant Garamond", serif; font-weight: 500; font-size: 19px;
    color: var(--title-lilac);
  }
  .front-title .main {
    display: block; margin-top: 4px;
    font-family: "Cinzel", serif; font-weight: 400; font-size: 32px; letter-spacing: 1px;
    color: var(--title-gold);
  }
</style>
</head>
<body>
<div class="canvas">
  <span class="crop-mark top left"></span>
  <span class="crop-mark top right"></span>
  <span class="crop-mark bottom left"></span>
  <span class="crop-mark bottom right"></span>

  <section class="book">
    <div class="rays"></div>
    <div class="back-cover"></div>
    <div class="winged-heart" role="img" aria-label="Illustration of a sparkling diamond heart with white angel wings glowing in light"></div>

    <div class="spine-title">
      <span class="spine-mark"></span>
      <span class="spine-text">THE SOUL OF A FAITHFUL SHEPHERD</span>
    </div>

    <div class="title-band">
      <h1 class="front-title">
        <span class="lead">the soul of a</span>
        <span class="main">Faithful Shepherd</span>
      </h1>
    </div>
  </section>
</div>
</body>
</html>
```